Harbin Cargo needs a business card design.

Design a double-sided business card for new freight business. On the front, would like to see our logo along with the following info:

Nathaniel Voskuhl
CEO/FOUNDER
617-552-0194
nathanielvoskuhl@harbin-cargo.example

On the reverse side, we would like to use the graphic image of our logo only without the Harbin Cargo name.

```html
<!DOCTYPE html>
<html lang="en">
<head>
<meta charset="utf-8">
<title>Harbin Cargo – Business Card</title>
<link rel="stylesheet" href="https://fonts.googleapis.com/css2?family=Michroma&family=Lato:wght@400;700&display=swap">
<style>
  :root {
    --navy: #1c1a5a;
    --navy-soft: #2d2b6e;
    --red: #b81e2b;
    --white: #ffffff;
    --ink: #2b2b36;
    --rule: #8a8a94;
    --faint: #f1f0f6;
    --backdrop: #4a4c50;
  }
  * { margin: 0; padding: 0; box-sizing: border-box; }
  html, body { width: 1200px; height: 900px; overflow: hidden; }
  body {
    background: var(--backdrop);
    position: relative;
    font-family: "Lato", sans-serif;
  }
  .card {
    position: absolute;
    width: 620px;
    height: 354px;
    border-radius: 26px;
    overflow: hidden;
    box-shadow: 0 12px 30px rgba(0,0,0,0.35);
  }
  .card-back { left: 110px; top: 60px; background: var(--navy); }
  .card-front { left: 470px; top: 486px; background: var(--white); }

  .faint-square {
    position: absolute;
    border-radius: 6px;
  }
  .card-back .faint-square {
    left: 70px;
    top: 90px;
    width: 210px;
    height: 210px;
    background: var(--navy-soft);
  }
  .card-front .faint-square {
    right: 40px;
    top: 120px;
    width: 150px;
    height: 150px;
    background: var(--faint);
  }

  .wordmark {
    position: absolute;
    left: 50px;
    top: 54px;
    display: flex;
    align-items: center;
    gap: 12px;
    font-family: "Michroma", sans-serif;
    font-size: 28px;
    line-height: 1.15;
    letter-spacing: 3px;
    text-transform: uppercase;
    color: var(--navy);
  }
  .wordmark-square { width: 18px; height: 18px; flex: none; background: var(--red); }

  .person {
    position: absolute;
    left: 170px;
    top: 148px;
    padding-left: 14px;
    border-left: 1.5px solid var(--red);
  }
  .person-name {
    font-family: "Michroma", sans-serif;
    font-size: 21px;
    text-transform: uppercase;
    letter-spacing: 1px;
    color: var(--navy);
    white-space: nowrap;
  }
  .person-surname { color: var(--red); margin-left: 14px; }
  .person-role {
    font-size: 15px;
    color: var(--ink);
    letter-spacing: 0.5px;
    margin-top: 2px;
  }

  .contact {
    position: absolute;
    left: 226px;
    top: 238px;
    padding-left: 12px;
    border-left: 1px solid var(--rule);
    list-style: none;
    font-size: 14px;
    color: var(--ink);
  }
  .contact li { display: flex; align-items: center; gap: 9px; line-height: 1.55; white-space: nowrap; }
  .contact svg { width: 13px; height: 13px; flex: none; }

  .edge-band { position: absolute; left: 0; bottom: 0; width: 620px; height: 30px; }
</style>
</head>
<body>

  <section class="card card-back" aria-label="Business card, reverse side">
    <div class="faint-square" aria-hidden="true"></div>
  </section>

  <section class="card card-front" aria-label="Business card, front side">
    <div class="faint-square" aria-hidden="true"></div>

    <div class="wordmark">
      <span class="wordmark-square"></span>
      <span>Harbin<br>Cargo</span>
    </div>

    <div class="person">
      <p class="person-name">Nathaniel<span class="person-surname">Voskuhl</span></p>
      <p class="person-role">CEO/FOUNDER</p>
    </div>

    <ul class="contact">
      <li>
        <svg viewBox="0 0 24 24" aria-hidden="true"><path fill="#b81e2b" d="M6.6 10.8a15.1 15.1 0 0 0 6.6 6.6l2.2-2.2c.3-.3.7-.4 1-.2 1.1.4 2.3.6 3.6.6.6 0 1 .4 1 1V20c0 .6-.4 1-1 1A17 17 0 0 1 3 4c0-.6.4-1 1-1h3.5c.6 0 1 .4 1 1 0 1.3.2 2.5.6 3.6.1.3 0 .7-.2 1z"/></svg>
        <span>617-552-0194</span>
      </li>
      <li>
        <svg viewBox="0 0 24 24" aria-hidden="true"><path fill="#b81e2b" d="M2 5h20v14H2z"/><path fill="none" stroke="#fff" stroke-width="2" d="M2 6l10 7 10-7"/></svg>
        <span>nathanielvoskuhl@harbin-cargo.example</span>
      </li>
    </ul>

    <svg class="edge-band" viewBox="0 0 620 30" aria-hidden="true">
      <polygon points="0,30 0,26 520,12 520,30" fill="#1c1a5a"/>
      <polygon points="524,12 620,6 620,30 524,30" fill="#b81e2b"/>
    </svg>
  </section>

</body>
</html>
```